Postcard Design

Marlow Painting-all types of painting and staining-house,deck and roof powerwashing-stone and masonry sealing-
30 years in business-licensed and insured
Ray Pettibone
pettiboneworks@brushmail.example
9145820731

Industry/Entity Type

Painting

```html
<!DOCTYPE html>
<html lang="en">
<head>
<meta charset="utf-8">
<title>Marlow Painting – Postcard</title>
<link rel="stylesheet" href="https://fonts.googleapis.com/css2?family=Open+Sans:wght@400;600&display=swap">
<style>
  :root {
    --backdrop: #b9b2d8;
    --card: #ffffff;
    --brand: #a698cb;
    --ink: #2b2b2b;
    --on-photo: #ffffff;
    --band: rgba(40, 34, 30, 0.72);
    --frame: #c5b9e0;
    --tag: #f4f3f5;
  }
  * { margin: 0; padding: 0; box-sizing: border-box; }
  html, body {
    width: 1200px; height: 928px; overflow: hidden;
    background: var(--backdrop);
    font-family: "Open Sans", Arial, sans-serif;
  }
  .stage { position: relative; width: 1200px; height: 928px; }

  /* ---------- Back of postcard ---------- */
  .postcard-back {
    position: absolute; left: 85px; top: 394px;
    width: 576px; height: 438px;
    background: var(--card); color: var(--ink);
  }
  .brand {
    position: absolute; display: flex; align-items: center; gap: 10px;
    color: var(--brand); font-weight: 600; letter-spacing: 2px;
    text-transform: uppercase; white-space: nowrap;
  }
  .brand-mark { background: var(--brand); flex: none; }
  .postcard-back .brand { left: 20px; top: 54px; font-size: 20px; }
  .postcard-back .brand-mark { width: 22px; height: 22px; }
  .postcard-back .tagline {
    position: absolute; left: 20px; top: 118px;
    font-size: 12.5px; text-transform: uppercase; white-space: nowrap;
  }
  .services { list-style: none; white-space: nowrap; }
  .services li { display: flex; align-items: center; gap: 4px; }
  .services svg { flex: none; }
  .postcard-back .services {
    position: absolute; left: 20px; top: 190px;
    font-size: 13px; line-height: 18.7px;
  }
  .contact { font-size: 12px; line-height: 17px; white-space: nowrap; }
  .contact .phone { font-size: 18px; letter-spacing: 2px; line-height: 24px; }
  .postcard-back .contact { position: absolute; left: 20px; top: 282px; }

  /* ---------- Front of postcard ---------- */
  .postcard-front {
    position: absolute; left: 526px; top: 100px;
    width: 575px; height: 438px; overflow: hidden;
  }
  .hero-photo {
    position: absolute; inset: 0;
    background:
      linear-gradient(180deg, rgba(0,0,0,0) 55%, rgba(120,90,60,0.55) 100%),
      linear-gradient(90deg, #7a5a45 0%, #b6a89a 14%, #d9dfd2 22%, #6f8d4e 38%, #4f6f34 70%, #3c5a29 100%);
  }
  .tag {
    position: absolute; left: 45px; top: 0;
    width: 136px; height: 118px;
  }
  .tag svg { position: absolute; inset: 0; }
  .tag .brand {
    left: 14px; top: 34px; font-size: 9.5px; letter-spacing: 0.6px; gap: 5px;
  }
  .tag .brand-mark { width: 9px; height: 9px; }
  .tag .tagline {
    position: absolute; left: 14px; top: 56px; width: 110px;
    font-size: 7.5px; line-height: 9.5px; color: var(--brand);
    text-transform: uppercase;
  }
  .snapshot {
    position: absolute; border: 5px solid var(--frame);
    box-shadow: 0 2px 6px rgba(0,0,0,0.35);
  }
  .snap-framing  { left: 358px; top: 62px;  width: 94px;  height: 128px; transform: rotate(-8deg);
                   background: linear-gradient(160deg, #e7ddc6, #b98d60 60%, #7a4a2e); }
  .snap-roof     { left: 452px; top: 24px;  width: 94px;  height: 126px; transform: rotate(6deg);
                   background: linear-gradient(200deg, #6fa3d8, #a9753f 55%, #5a3a22); }
  .snap-shingles { left: 428px; top: 170px; width: 124px; height: 80px;  transform: rotate(5deg);
                   background: linear-gradient(150deg, #b8cde0, #c6603e 55%, #8e3a24); }
  .snap-plaster  { left: 412px; top: 254px; width: 128px; height: 92px;  transform: rotate(-7deg);
                   background: linear-gradient(120deg, #3b4f6a, #cfc2a6 50%, #e8dcc0); }
  .info-band {
    position: absolute; left: 0; bottom: 0; width: 100%; height: 76px;
    background: var(--band); color: var(--on-photo);
  }
  .info-band .services {
    position: absolute; left: 30px; top: 18px;
    font-size: 10px; line-height: 13.5px;
  }
  .info-band .contact {
    position: absolute; right: 16px; top: 12px;
    font-size: 11.5px; line-height: 15.5px;
  }
  .info-band .contact .phone { font-size: 18.5px; line-height: 22px; }
</style>
</head>
<body>
<main class="stage">

  <section class="postcard-back" aria-label="Postcard back">
    <div class="brand"><span class="brand-mark"></span>Marlow Painting</div>
    <p class="tagline">30 years in business-licensed and insured</p>
    <ul class="services">
      <li><svg width="12" height="12" viewBox="0 0 12 12"><rect x="0.5" y="0.5" width="11" height="11" fill="none" stroke="currentColor"/><path d="M2.5 6 L5 8.5 L9.5 3" fill="none" stroke="currentColor" stroke-width="1.4"/></svg>All types of painting and staining-house</li>
      <li><svg width="12" height="12" viewBox="0 0 12 12"><rect x="0.5" y="0.5" width="11" height="11" fill="none" stroke="currentColor"/><path d="M2.5 6 L5 8.5 L9.5 3" fill="none" stroke="currentColor" stroke-width="1.4"/></svg>Deck and roof powerwashing-stone</li>
      <li><svg width="12" height="12" viewBox="0 0 12 12"><rect x="0.5" y="0.5" width="11" height="11" fill="none" stroke="currentColor"/><path d="M2.5 6 L5 8.5 L9.5 3" fill="none" stroke="currentColor" stroke-width="1.4"/></svg>Masonry sealing</li>
    </ul>
    <div class="contact">
      <p>Ray Pettibone</p>
      <p>pettiboneworks@brushmail.example</p>
      <p class="phone">9145820731</p>
    </div>
  </section>

  <section class="postcard-front" aria-label="Postcard front">
    <div class="hero-photo" role="img" aria-label="Photo of a wooden deck with patio chairs and potted flowers beside a house, trees behind"></div>

    <div class="tag">
      <svg width="136" height="118" viewBox="0 0 136 118"><path d="M0 0 H136 V118 L68 100 L0 118 Z" fill="var(--tag)"/></svg>
      <div class="brand"><span class="brand-mark"></span>Marlow Painting</div>
      <p class="tagline">30 years in business-<br>licensed and insured</p>
    </div>

    <div class="snapshot snap-framing" role="img" aria-label="Photo of a worker on a timber house frame"></div>
    <div class="snapshot snap-roof" role="img" aria-label="Photo of a worker repairing a wooden roof"></div>
    <div class="snapshot snap-shingles" role="img" aria-label="Photo of a worker on a red tiled roof"></div>
    <div class="snapshot snap-plaster" role="img" aria-label="Photo of a worker in a hard hat finishing a wall"></div>

    <div class="info-band">
      <ul class="services">
        <li><svg width="10" height="10" viewBox="0 0 12 12"><rect x="0.5" y="0.5" width="11" height="11" fill="none" stroke="currentColor"/><path d="M2.5 6 L5 8.5 L9.5 3" fill="none" stroke="currentColor" stroke-width="1.4"/></svg>All types of painting and staining-house</li>
        <li><svg width="10" height="10" viewBox="0 0 12 12"><rect x="0.5" y="0.5" width="11" height="11" fill="none" stroke="currentColor"/><path d="M2.5 6 L5 8.5 L9.5 3" fill="none" stroke="currentColor" stroke-width="1.4"/></svg>Deck and roof powerwashing-stone</li>
        <li><svg width="10" height="10" viewBox="0 0 12 12"><rect x="0.5" y="0.5" width="11" height="11" fill="none" stroke="currentColor"/><path d="M2.5 6 L5 8.5 L9.5 3" fill="none" stroke="currentColor" stroke-width="1.4"/></svg>Masonry sealing</li>
      </ul>
      <div class="contact">
        <p>Ray Pettibone</p>
        <p>pettiboneworks@brushmail.example</p>
        <p class="phone">9145820731</p>
      </div>
    </div>
  </section>

</main>
</body>
</html>
```